Quorvex - Automated robotic Inspection with AI need new business cards

We need a new design of our business cards. The company is focused on automated quality control at high speed with unmatched results. We have a logo but need a more forward leaning business card that shows that we are delivering cutting edge technology.

Contact Information for Business Card

Name
Position
Adress
Phone
Email
e.g.
Lena Holmqvist
Chief Financial Officer (CFO)

Quorvex Sweden AB
Bruksvägen 14, SE-175 43 JÄRFÄLLA, Sweden
Mobile: +46735 21 47 83 | Office: +46 8 61 94 27
www.quorvex-example.com

Font styles to use
Sans Serif

```html
<!DOCTYPE html>
<html lang="en">
<head>
<meta charset="UTF-8">
<title>Quorvex Business Card</title>
<link rel="stylesheet" href="https://fonts.googleapis.com/css2?family=Roboto:wght@400;500;700&display=swap">
<style>
  :root {
    --stage: #d8d6d7;
    --paper: #ffffff;
    --brand: #15527a;
    --brand-deep: #134f73;
    --brand-soft: #185a80;
    --ink-grey: #8e8e8e;
    --on-brand: #ffffff;
  }
  * { margin: 0; padding: 0; box-sizing: border-box; }
  html, body {
    width: 1200px; height: 1100px; overflow: hidden;
    background: var(--stage);
    font-family: "Roboto", Arial, sans-serif;
  }
  .card {
    position: absolute; left: 259px; width: 705px; height: 406px;
    border-radius: 18px; overflow: hidden;
    box-shadow: 0 2px 6px rgba(0,0,0,0.25);
  }
  .card--front { top: 114px; background: var(--paper); }
  .card--back {
    top: 560px;
    background: radial-gradient(ellipse at 55% 45%, var(--brand-soft) 0%, var(--brand-deep) 70%);
  }

  .brand-mark {
    position: absolute; display: flex; align-items: center;
    font-weight: 700; letter-spacing: 1px;
  }
  .brand-mark__dot { border-radius: 50%; flex: none; }
  .card--front .brand-mark {
    left: 52px; top: 172px; gap: 14px;
    font-size: 52px; color: var(--brand);
  }
  .card--front .brand-mark__dot { width: 36px; height: 36px; background: var(--brand); }
  .card--back .brand-mark {
    left: 50%; top: 148px; transform: translateX(-50%); gap: 22px;
    font-size: 78px; color: var(--on-brand);
  }
  .card--back .brand-mark__dot { width: 54px; height: 54px; background: var(--on-brand); }

  .divider {
    position: absolute; left: 368px; top: 94px; width: 1.5px; height: 220px;
    background: var(--brand);
  }
  .contact { position: absolute; left: 391px; top: 88px; color: var(--ink-grey); }
  .contact__name { font-size: 25px; font-weight: 500; color: var(--brand); line-height: 30px; }
  .contact__role { font-size: 18px; line-height: 22px; }
  .contact__address { margin-top: 10px; font-size: 18px; line-height: 22.5px; }
  .contact__list { list-style: none; margin-top: 9px; font-size: 17.5px; }
  .contact__list li { display: flex; align-items: center; gap: 5px; height: 24px; }
  .contact__list svg { width: 14px; height: 14px; fill: var(--brand); flex: none; }

  .card__url {
    position: absolute; left: 0; right: 0; top: 357px; text-align: center;
    color: var(--on-brand); font-size: 17px; font-weight: 500;
  }
</style>
</head>
<body>
  <section class="card card--front">
    <div class="brand-mark"><span class="brand-mark__dot"></span>Quorvex</div>
    <div class="divider"></div>
    <div class="contact">
      <p class="contact__name">Lena Holmqvist</p>
      <p class="contact__role">Chief Financial Officer (CFO)</p>
      <p class="contact__address">Quorvex Sweden AB<br>Bruksvägen 14<br>SE-175 43 JÄRFÄLLA, Sweden</p>
      <ul class="contact__list">
        <li><svg viewBox="0 0 14 14"><path d="M3 0h8v14H3z M4.5 1.5v10h5v-10z M6.3 12h1.4v1h-1.4z"/></svg>+46735 21 47 83</li>
        <li><svg viewBox="0 0 14 14"><path d="M3 0.5l2.3 2.8-1.3 1.8c.8 2 2.2 3.6 4.3 4.7l1.7-1.3 2.9 2.2-1.4 2.5C6.3 13 1.4 8.3.6 2.2z"/></svg>+46 8 61 94 27</li>
        <li><svg viewBox="0 0 14 14"><path d="M0 2.5h14v9H0z M1.2 3.5l5.8 4.3 5.8-4.3v-.1H1.2z" fill-rule="evenodd"/></svg>info@quorvex-example.com</li>
        <li><svg viewBox="0 0 14 14"><path d="M7 .5a6.5 6.5 0 1 0 0 13 6.5 6.5 0 0 0 0-13zm-.6 1.3v2.3H4.5c.4-1.2 1-2 1.9-2.3zm1.2 0c.9.3 1.5 1.1 1.9 2.3H7.6zM3.3 4.1H1.9a5.3 5.3 0 0 1 2-2 7 7 0 0 0-.6 2zm7.4 0a7 7 0 0 0-.6-2 5.3 5.3 0 0 1 2 2zM1.5 5.3h1.7v3.4H1.5zm2.9 0h2v3.4h-2zm3.2 0h2v3.4h-2zm3.2 0h1.7v3.4h-1.7zM1.9 9.9h1.4a7 7 0 0 0 .6 2 5.3 5.3 0 0 1-2-2zm2.6 0h1.9v2.3c-.9-.3-1.5-1.1-1.9-2.3zm3.1 0h1.9c-.4 1.2-1 2-1.9 2.3zm3.1 0h1.4a5.3 5.3 0 0 1-2 2 7 7 0 0 0 .6-2z"/></svg>www.quorvex-example.com</li>
      </ul>
    </div>
  </section>

  <section class="card card--back">
    <div class="brand-mark"><span class="brand-mark__dot"></span>Quorvex</div>
    <p class="card__url">www.quorvex-example.com</p>
  </section>
</body>
</html>
```